Web Design Project - Investor Services

I would like a simple and elegant web design for my company "Corvalo Management". The company will provide services to Corporate and Institutional investors for their needs with local/foreign investment vehicles. The website will have four pages to start: home, about us, services, contact.
I already chose a logo, and I will attach the source file. The color that I will most probably use for the logo will be blue, and i also like grey with a white background. For the website I would like to see light colors, maybe light green or grey, with the logo either in blue, grey or white (depeding on the background).
Target Market(s)
Investment managers and tax/legal advisors from top firms. This is the reason why I want something simple and elegant.
Industry/Entity Type
Investment
Requirements
Nice to have
- I do not want many pictures in the website, but I might include a couple of pictures of Madrid and maybe a picture of myself in the about us page (still deciding). I will attach some pictures of Madrid that I like, but feel free to search for others - i have others but i am not able to attach all of them.

```html
<!DOCTYPE html>
<html lang="en">
<head>
<meta charset="utf-8">
<title>Corvalo Management</title>
<link rel="stylesheet" href="https://fonts.googleapis.com/css2?family=Open+Sans:wght@300;400;800&display=swap">
<style>
  :root {
    --page-bg: #5a5b5f;
    --band-bg: #545557;
    --band-text: #47484a;
    --accent-green: #3dcb70;
    --text-white: #ffffff;
    --footer-text: #3a3b3d;
    --footer-icon: #404143;
  }
  * { margin: 0; padding: 0; box-sizing: border-box; }
  html, body {
    width: 1200px;
    height: 858px;
    overflow: hidden;
    background: var(--page-bg);
    font-family: "Open Sans", Arial, sans-serif;
  }
  .page {
    position: relative;
    width: 1200px;
    height: 858px;
  }
  .side-band {
    position: absolute;
    left: 955px;
    top: 0;
    width: 140px;
    height: 858px;
    background: var(--band-bg);
  }
  .side-tagline {
    position: absolute;
    left: 1024px;
    top: 16px;
    writing-mode: vertical-rl;
    font-size: 45px;
    font-weight: 800;
    line-height: 1;
    color: var(--band-text);
    letter-spacing: 0.5px;
  }
  .site-header {
    position: absolute;
    left: 200px;
    top: 30px;
    width: 800px;
    height: 56px;
  }
  .brand-name {
    position: absolute;
    left: 0;
    top: 8px;
    font-size: 34px;
    font-weight: 300;
    color: var(--text-white);
    letter-spacing: 0.5px;
  }
  .main-nav {
    position: absolute;
    right: 0;
    top: 20px;
    display: flex;
    gap: 30px;
    list-style: none;
  }
  .main-nav a {
    font-size: 13px;
    color: var(--accent-green);
    text-decoration: none;
  }
  .hero-photo {
    position: absolute;
    left: 200px;
    top: 105px;
    width: 800px;
    height: 449px;
    background: linear-gradient(180deg, #6f7286 0%, #9b8fa0 18%, #e6a9ab 35%, #f1b1b0 55%, #b88a8c 72%, #3a3236 85%, #151515 100%);
  }
  .welcome {
    position: absolute;
    left: 200px;
    top: 586px;
    width: 800px;
  }
  .welcome-title {
    font-size: 27px;
    font-weight: 300;
    color: var(--accent-green);
    line-height: 1.3;
  }
  .welcome-text {
    margin-top: 10px;
    font-size: 13.2px;
    line-height: 22px;
    color: var(--text-white);
  }
  .site-footer {
    position: absolute;
    left: 955px;
    top: 808px;
    width: 140px;
    text-align: center;
  }
  .copyright {
    font-size: 9px;
    color: var(--footer-text);
    letter-spacing: -0.2px;
  }
  .social-links {
    display: flex;
    justify-content: center;
    gap: 6px;
    margin-top: 6px;
    padding-left: 10px;
  }
  .social-links span {
    width: 15px;
    height: 15px;
    background: var(--footer-icon);
    border-radius: 2px;
  }
</style>
</head>
<body>
<div class="page">
  <div class="side-band"></div>
  <div class="side-tagline">Worldwide Investment</div>

  <header class="site-header">
    <div class="brand-name">Corvalo Management</div>
    <ul class="main-nav">
      <li><a href="#about">About Us</a></li>
      <li><a href="#services">Services</a></li>
      <li><a href="#contact">Contact</a></li>
    </ul>
  </header>

  <div class="hero-photo" role="img" aria-label="Madrid skyline with four business towers at dusk under a pink sky"></div>

  <section class="welcome">
    <h1 class="welcome-title">Welcome to Corvalo Management</h1>
    <p class="welcome-text">Lorem ipsum dolor sit amet, consectetur adipiscing elit. Vestibulum porttitor ligula non metus commodo ultrices. Curabitur elem entu libero eget lacus lobortis gravida. Mauris sem ante, scelerisque a aliquam vitae, commodo at eros. Donec suscipit sagittis ultricies. Fusce vitae mi risus. Praesent diam nunc, vestibulum lobortis lobortis a, viverra et nunc. Cras ornare nibh vitae diam luctus at iaculis tortor lacinia. Phasellus id blandit leo. Nunc fringilla, arcu sit amet ullamcorper vulputate, nulla diam auctor tellu et tempus. Justo purus eget odio. duis eget neque ac urna semper tinci dunt a em eget nibh ni u elitm nunc, vestib us lobort.</p>
  </section>

  <footer class="site-footer">
    <p class="copyright">©2013 Corvalo Management.</p>
    <div class="social-links" aria-label="Social links">
      <span></span><span></span><span></span>
    </div>
  </footer>
</div>
</body>
</html>
```